Funeral Services Site

We need a website for a Funeral Services company. The old website is: www.rouwcentrumkorvelaer.be We need the same structure and text.

Target Market(s)

Customers.

Coding

Coded - Design and coding required

Number of Pages Required

4 page

Font styles to use
Serif
Sans Serif
Script

```html
<!DOCTYPE html>
<html lang="en">
<head>
<meta charset="utf-8">
<title>Funeral home Verbeke bvba</title>
<link href="https://fonts.googleapis.com/css2?family=Poppins:wght@400;500;600&display=swap" rel="stylesheet">
<style>
:root{
  --black:#000;
  --white:#fff;
  --grey:#5e5e5e;
  --grey-dark:#3a3a3a;
  --ghost:#2e2e2e;
  --ghost-light:#3d3d3d;
}
*{box-sizing:border-box;margin:0;padding:0}
html,body{width:1200px;height:3354px;overflow:hidden;background:var(--black);font-family:'Poppins',sans-serif;color:var(--white)}
.page{position:relative;width:1200px;height:3354px;overflow:hidden}
.abs{position:absolute}
a{color:inherit;text-decoration:none}

.topbar{left:0;top:0;width:1200px;height:42px;background:rgba(70,70,70,.85);z-index:3;font-size:15px;display:flex;align-items:center;padding:0 89px;justify-content:space-between}
.topbar .info{display:flex;gap:12px;align-items:center}
.topbar .dots{display:flex;gap:9px}
.topbar .dots span{width:11px;height:11px;border-radius:50%;background:var(--white);display:block}

.hero{left:0;top:0;width:1200px;height:720px;background:radial-gradient(ellipse at 50% 55%,#8a7458 0%,#4f3d2a 45%,#22190f 100%)}
.brand{left:94px;top:74px;display:flex;align-items:center;gap:14px;z-index:3}
.brand .mark{width:70px;height:70px;border-radius:50%;background:var(--white)}
.brand .name{font-size:26px;font-weight:500;line-height:36px}
.nav{right:100px;top:100px;display:flex;gap:40px;font-size:16px;font-weight:500;z-index:3;align-items:center}
.hero-title{left:0;width:1200px;top:278px;text-align:center;font-size:45px;font-weight:500}
.hero-sub{left:0;width:1200px;top:342px;text-align:center;font-size:34px}
.btn{display:inline-flex;align-items:center;justify-content:center;gap:10px;height:54px;border-radius:27px;font-size:18px;font-weight:500;background:var(--grey);color:var(--white)}
.btn .dot{width:16px;height:16px;border-radius:50%;background:var(--white)}
.btn-outline{background:transparent;border:3px solid var(--white)}
.seal{width:50px;height:50px;border-radius:50%;background:var(--white);border:3px solid var(--grey-dark)}

.ghost{font-size:92px;font-weight:500;color:var(--ghost);line-height:1;white-space:nowrap}
.h2{font-size:35px;font-weight:500;line-height:1}
.para{font-size:16px;line-height:36px;text-align:justify}

.services-bg{left:0;top:1390px;width:1200px;height:680px;background:linear-gradient(180deg,#3a3026 0%,#2a241d 50%,#1c1c1c 100%)}
.card{width:313px;height:170px;border:2px solid var(--white);border-radius:8px;padding:48px 14px 0 12px;font-size:16px;line-height:31px;text-align:justify;background:rgba(0,0,0,.15)}
.card.small{font-size:13px;line-height:30px;padding-top:44px}
.badge{width:88px;height:88px;border-radius:50%;border:2px solid var(--white);background:#2a2a2a;display:flex;align-items:center;justify-content:center}

.footer-bg{left:0;top:2760px;width:1200px;height:594px;background:linear-gradient(180deg,#1a1f14 0%,#161a12 60%,#0e0e0e 100%)}
.contact{width:260px;text-align:center;font-size:18px;line-height:28px}
.ring{width:96px;height:96px;margin:0 auto 8px;border-radius:50%;background:var(--grey);border:6px solid #ddd;display:flex;align-items:center;justify-content:center}
.flinks{left:0;width:1200px;top:3218px;text-align:center;font-size:18px;word-spacing:4px}
.copy{left:0;width:1200px;top:3255px;text-align:center;font-size:16px}
.social{left:530px;top:3292px;display:flex;gap:8px}
.social span{width:30px;height:30px;border:2px solid var(--white);border-radius:50%;display:block}
</style>
</head>
<body>
<div class="page">

  <div class="abs hero" role="img" aria-label="Photo of a candlelit chapel with a cross and white flowers on a coffin"></div>

  <div class="abs topbar">
    <div class="info"><span>● Lindelaan 18, 3790 Elsweg (Haverbeek)</span><span>|</span><span>✉ Email : contact@rouwcentrumverbeke.be</span></div>
    <div class="dots"><span></span><span></span><span></span><span></span></div>
  </div>

  <div class="abs brand"><span class="mark"></span><span class="name">Funeral home<br>Verbeke bvba</span></div>
  <nav class="abs nav"><a>Home</a><a>About Us</a><a>Condole Online</a><a>Order Flowers</a><a>Contact</a>
    <svg width="16" height="16" viewBox="0 0 16 16"><circle cx="6.5" cy="6.5" r="5" fill="none" stroke="#fff" stroke-width="2"/><line x1="10" y1="10" x2="15" y2="15" stroke="#fff" stroke-width="2"/></svg></nav>

  <h1 class="abs hero-title">FUNERAL HOME VERBEKE BVBA</h1>
  <p class="abs hero-sub">a personal service in farewell guidance</p>
  <a class="abs btn" style="left:389px;top:408px;width:206px">Order Flowers <span class="dot" style="border-radius:2px"></span></a>
  <a class="abs btn btn-outline" style="left:607px;top:408px;width:205px">Contact Us <span class="dot"></span></a>

  <svg class="abs" style="left:0;top:620px" width="1200" height="110" viewBox="0 0 1200 110">
    <path d="M0 110 Q600 -10 1200 110 Z" fill="#000"/>
    <path d="M110 80 Q600 20 1090 80 Q600 35 110 80 Z" fill="#777"/>
  </svg>
  <div class="abs seal" style="left:575px;top:624px"></div>

  <svg class="abs" style="left:52px;top:825px" width="456" height="456" viewBox="0 0 456 456">
    <path d="M228 8 A220 220 0 0 1 446 260" fill="none" stroke="#5a5a5a" stroke-width="12"/>
    <path d="M400 360 A220 220 0 0 1 260 446" fill="none" stroke="#5a5a5a" stroke-width="22"/>
    <path d="M100 420 A220 220 0 0 1 22 150" fill="none" stroke="#5a5a5a" stroke-width="16"/>
    <circle cx="228" cy="228" r="192" fill="none" stroke="#444" stroke-width="4"/>
  </svg>
  <div class="abs" style="left:91px;top:865px;width:378px;height:378px;border-radius:50%;background:linear-gradient(180deg,#b9bcc0 0%,#7d6a5c 45%,#3f5a2d 100%)" role="img" aria-label="Photo of the funeral home building with a willow tree and parked cars"></div>
  <div class="abs ghost" style="left:533px;top:845px">ABOUT US</div>
  <h2 class="abs h2" style="left:533px;top:905px">ABOUT US</h2>
  <p class="abs para" style="left:532px;top:957px;width:574px">Sed ut perspiciatis unde omnis iste natus error sit voluptatem accusantium doloremque laudantium, totam rem aperiam, eaque ipsa quae ab illo inventore veritatis et quasi architecto beatae vitae dicta sunt explicabo. Nemo enim ipsam voluptatem quia voluptas sit aspernatur aut odit aut</p>
  <a class="abs btn" style="left:532px;top:1163px;width:206px">Read More <span class="dot"></span></a>

  <div class="abs services-bg" role="img" aria-label="Dark photo of a chapel with a cross and white flowers"></div>
  <svg class="abs" style="left:0;top:1385px" width="1200" height="100" viewBox="0 0 1200 100">
    <path d="M0 0 H1200 V5 Q600 -5 0 100 Z" fill="#000"/>
    <path d="M0 100 Q500 10 1200 5 Q500 0 0 50 Z" fill="#6a6a6a"/>
  </svg>
  <svg class="abs" style="left:0;top:1975px" width="1200" height="100" viewBox="0 0 1200 100">
    <path d="M0 100 H1200 V0 Q700 90 0 95 Z" fill="#000"/>
    <path d="M1200 0 Q700 70 200 95 Q700 90 1200 40 Z" fill="#6a6a6a"/>
  </svg>
  <div class="abs ghost" style="left:0;width:1200px;text-align:center;top:1495px;color:var(--ghost-light)">OUR SERVICES</div>
  <h2 class="abs h2" style="left:0;width:1200px;text-align:center;top:1542px">OUR SERVICES</h2>
  <p class="abs" style="left:200px;width:800px;top:1600px;text-align:center;font-size:16px;line-height:36px">At vero eos et accusamus et iusto odio dignissimos ducimus qui blanditiis praesentium voluptatum deleniti atque corrupti quos molestias excepturi sint</p>

  <svg class="abs" style="left:40px;top:1793px" width="36" height="24" viewBox="0 0 36 24"><path d="M34 12 H3 M13 2 L3 12 L13 22" fill="none" stroke="#fff" stroke-width="2.5"/></svg>
  <svg class="abs" style="left:1124px;top:1793px" width="36" height="24" viewBox="0 0 36 24"><path d="M2 12 H33 M23 2 L33 12 L23 22" fill="none" stroke="#fff" stroke-width="2.5"/></svg>

  <div class="abs card" style="left:89px;top:1742px">funeral liturgy with priest (on Tuesday and Friday in the parishes of the Molenbeek dean.</div>
  <div class="abs card small" style="left:443px;top:1742px">funeral liturgy with priest / leader, leader in the funeral liturgy in your parish church, other church or crematorium from Monday to Saturday</div>
  <div class="abs card" style="left:797px;top:1742px;padding-left:14px">farewell celebration in our auditorium, crematorium or other location.</div>

  <div class="abs badge" style="left:133px;top:1698px"><svg width="40" height="40" viewBox="0 0 40 40" fill="none" stroke="#fff" stroke-width="2"><path d="M20 4 V10 M17 7 H23 M10 36 V18 L20 10 L30 18 V36 Z M16 36 V28 H24 V36 M4 36 H36"/></svg></div>
  <div class="abs badge" style="left:487px;top:1698px"><svg width="40" height="40" viewBox="0 0 40 40" fill="none" stroke="#fff" stroke-width="2"><path d="M20 3 V9 M17 6 H23 M12 36 V18 L20 9 L28 18 V36 Z M17 36 V28 H23 V36 M4 36 H36"/></svg></div>
  <div class="abs badge" style="left:841px;top:1698px"><svg width="40" height="44" viewBox="0 0 40 44"><path d="M20 4 C12 4 8 10 8 15 C8 24 20 34 20 34 C20 34 32 24 32 15 C32 10 28 4 20 4 Z" fill="#fff"/><circle cx="20" cy="15" r="4" fill="#2a2a2a"/><ellipse cx="20" cy="38" rx="14" ry="4" fill="none" stroke="#fff" stroke-width="2"/></svg></div>

  <div class="abs ghost" style="left:85px;top:2235px">OUR SHOP</div>
  <h2 class="abs h2" style="left:89px;top:2284px">RESERVE FLOWER ARRANGEMENT</h2>
  <p class="abs para" style="left:89px;top:2337px;width:576px;font-size:15.5px;letter-spacing:-0.1px">In the funeral home there is always an engaging selection of floral arrangements and wreaths . If you want to order fresh flowers, consult the catalog in the store or complete the order form on this page .</p>
  <a class="abs btn" style="left:89px;top:2470px;width:206px">Order Flowers <span class="dot"></span></a>

  <svg class="abs" style="left:699px;top:2173px" width="456" height="456" viewBox="0 0 456 456">
    <path d="M228 8 A220 220 0 0 1 446 260" fill="none" stroke="#5a5a5a" stroke-width="12"/>
    <path d="M400 360 A220 220 0 0 1 260 446" fill="none" stroke="#5a5a5a" stroke-width="22"/>
    <path d="M100 420 A220 220 0 0 1 22 150" fill="none" stroke="#5a5a5a" stroke-width="16"/>
    <circle cx="228" cy="228" r="192" fill="none" stroke="#444" stroke-width="4"/>
  </svg>
  <div class="abs" style="left:738px;top:2212px;width:378px;height:378px;border-radius:50%;background:radial-gradient(circle at 45% 55%,#e8e0b0 0%,#c9a838 35%,#8a6a45 70%,#5a4630 100%)" role="img" aria-label="Photo of a funeral arrangement with white lilies and yellow flowers"></div>

  <div class="abs footer-bg" role="img" aria-label="Dark photo of a cemetery with trees and a cross"></div>
  <svg class="abs" style="left:0;top:2730px" width="1200" height="120" viewBox="0 0 1200 120">
    <path d="M0 0 H1200 V80 Q600 20 0 120 Z" fill="#000"/>
    <path d="M10 110 Q600 10 1200 70 Q600 28 10 110 Z" fill="#777"/>
  </svg>
  <div class="abs seal" style="left:575px;top:2727px"></div>

  <div class="abs" style="left:562px;top:2895px;width:76px;height:76px;border-radius:50%;background:var(--white)"></div>
  <h3 class="abs" style="left:0;width:1200px;top:2985px;text-align:center;font-size:26px;font-weight:500">FUNERAL HOME VERBEKE BVBA</h3>

  <div class="abs contact" style="left:142px;top:3044px">
    <div class="ring"><svg width="34" height="40" viewBox="0 0 34 40" fill="none" stroke="#ddd" stroke-width="2"><path d="M17 2 C9 2 5 8 5 13 C5 22 17 32 17 32 C17 32 29 22 29 13 C29 8 25 2 17 2 Z"/><circle cx="17" cy="13" r="4"/><ellipse cx="17" cy="35" rx="12" ry="3"/></svg></div>
    Lindelaan 18, 3790<br>Elsweg (Haverbeek)
  </div>
  <div class="abs contact" style="left:447px;top:3044px;width:320px">
    <div class="ring"><svg width="44" height="32" viewBox="0 0 44 32" fill="none" stroke="#ddd" stroke-width="2"><rect x="2" y="2" width="40" height="28"/><path d="M2 2 L22 18 L42 2 M2 30 L17 14 M42 30 L27 14"/></svg></div>
    Email:<br>contact@rouwcentrumverbeke.be
  </div>
  <div class="abs contact" style="left:815px;top:3044px">
    <div class="ring"><svg width="36" height="36" viewBox="0 0 36 36" fill="none" stroke="#ddd" stroke-width="2"><path d="M8 3 L14 9 L10 14 C12 20 16 24 22 26 L27 22 L33 28 L28 33 C16 32 4 20 3 8 Z"/></svg></div>
    Phone:<br>012 34 56 78
  </div>

  <p class="abs flinks">Home &nbsp; | &nbsp; About Us &nbsp; | &nbsp; Condole Online &nbsp; | &nbsp; Order Flowers &nbsp; | &nbsp; Contact</p>
  <p class="abs copy">© Funeral home Verbeke &nbsp;2019. All rights reserved</p>
  <div class="abs social"><span></span><span></span><span></span><span></span></div>

</div>
</body>
</html>
```